KMW Plumbing and Roofing

design a fresh modern card for a young plumbing business looking to break into the market.
Must include the logo in the attached file
Bryce Olmo Verity
Phone number 0413962840
Vic Licence no 63194
email......

New Homes & Renovations
General Plumbing & Maintenance
Solar Hot Water Units
Roofing & Guttering (new and replacement)

Industry/Entity Type

Business

```html
<!DOCTYPE html>
<html lang="en">
<head>
<meta charset="utf-8">
<title>KMW Plumbing and Roofing – Business Card</title>
<link rel="stylesheet" href="https://fonts.googleapis.com/css2?family=Titillium+Web:wght@400;600&display=swap">
<style>
  :root {
    --backdrop: #3b3b3d;
    --card: #0e0e0f;
    --gold: #d9a233;
    --blue: #1c6d9f;
    --blue-light: #2a86bd;
    --white: #f4f4f4;
    --icon-dark: #1a1a1a;
  }
  * { box-sizing: border-box; margin: 0; padding: 0; }
  html, body {
    width: 1200px; height: 800px; overflow: hidden;
    background: var(--backdrop);
    font-family: "Titillium Web", Arial, sans-serif;
  }
  .canvas {
    position: relative; width: 1200px; height: 800px;
    display: flex; justify-content: center; align-items: center; gap: 70px;
  }
  .card {
    position: relative; width: 330px; height: 560px;
    background: var(--card);
    box-shadow: 0 14px 30px rgba(0,0,0,.45);
    overflow: hidden;
  }
  .card__band {
    position: absolute; left: 0; right: 0; bottom: 0; height: 20px;
    background: var(--blue);
  }
  .brand {
    display: flex; align-items: center; gap: 12px;
  }
  .brand__dot {
    flex: none; border-radius: 50%; background: var(--blue-light);
  }
  .brand__name {
    color: var(--white); font-weight: 600; line-height: 1.15;
  }

  /* front */
  .card--front .brand { position: absolute; left: 34px; top: 92px; }
  .card--front .brand__dot { width: 52px; height: 52px; }
  .card--front .brand__name { font-size: 20px; }
  .holder {
    position: absolute; left: 34px; top: 222px;
    color: var(--gold); font-size: 28px; font-weight: 400;
    letter-spacing: .5px; text-transform: uppercase;
  }
  .contact {
    position: absolute; left: 34px; top: 300px; list-style: none;
  }
  .contact__item {
    display: flex; align-items: center; gap: 14px;
    color: var(--white); font-size: 16px; margin-bottom: 26px;
  }
  .contact__icon {
    width: 30px; height: 30px; border-radius: 50%;
    background: var(--gold); display: flex; align-items: center; justify-content: center;
  }
  .licence {
    position: absolute; left: 34px; top: 446px;
    color: var(--blue-light); font-size: 20px;
  }
  .licence__number { color: var(--white); font-size: 22px; margin-left: 4px; }

  /* back */
  .card--back .brand {
    position: absolute; left: 0; right: 0; top: 80px;
    flex-direction: column; gap: 22px; text-align: center;
  }
  .card--back .brand__dot { width: 140px; height: 140px; }
  .card--back .brand__name { font-size: 26px; }
  .services {
    position: absolute; left: 0; right: 0; top: 400px;
    list-style: none; text-align: center;
    color: var(--white); font-size: 14px; line-height: 1.45;
  }
</style>
</head>
<body>
<main class="canvas">
  <article class="card card--front">
    <div class="brand">
      <span class="brand__dot"></span>
      <span class="brand__name">KMW Plumbing and Roofing</span>
    </div>
    <h1 class="holder">Bryce Olmo Verity</h1>
    <ul class="contact">
      <li class="contact__item">
        <span class="contact__icon">
          <svg width="16" height="16" viewBox="0 0 24 24" aria-hidden="true"><path fill="var(--icon-dark)" d="M6.6 10.8a15.1 15.1 0 0 0 6.6 6.6l2.2-2.2a1 1 0 0 1 1-.25 11.4 11.4 0 0 0 3.6.57 1 1 0 0 1 1 1V20a1 1 0 0 1-1 1A17 17 0 0 1 3 4a1 1 0 0 1 1-1h3.5a1 1 0 0 1 1 1c0 1.25.2 2.45.57 3.57a1 1 0 0 1-.25 1z"/></svg>
        </span>
        0413962840
      </li>
      <li class="contact__item">
        <span class="contact__icon">
          <svg width="16" height="16" viewBox="0 0 24 24" aria-hidden="true"><path fill="var(--icon-dark)" d="M3 5h18a1 1 0 0 1 1 1v12a1 1 0 0 1-1 1H3a1 1 0 0 1-1-1V6a1 1 0 0 1 1-1zm1 2.2V17h16V7.2l-8 5.3z"/><path fill="var(--icon-dark)" d="M4 7l8 5.3L20 7z" opacity=".6"/></svg>
        </span>
        bryceverity@kmwplumbing.com
      </li>
    </ul>
    <p class="licence">Vic Licence No.<span class="licence__number">63194</span></p>
    <div class="card__band"></div>
  </article>

  <article class="card card--back">
    <div class="brand">
      <span class="brand__dot"></span>
      <span class="brand__name">KMW Plumbing and Roofing</span>
    </div>
    <ul class="services">
      <li>New Homes &amp; Renovations</li>
      <li>General Plumbing &amp; Maintenance</li>
      <li>Solar Hot Water Units</li>
      <li>Roofing &amp; Guttering (New and Replacement)</li>
    </ul>
    <div class="card__band"></div>
  </article>
</main>
</body>
</html>
```